IT supplier clean wordpress website - payment guaranteed

Clean website design for a wordpress based website
Design only - PSD delivery with images

current website: www.quilmo.net
please use your imagination and try something out of the box...
We like https://trevanly.com.au as look and feel, but you don't have to copy it, you can be creative

We like the navigation header and the phone number, but do not need 'instant quote' so the 1300 phone number and the 'lock' icon for login can be on the same line

Site Map:
IT support
VoIP
Internet and Data
Cloud hosting
About
Contact

Our logo is attached, it can be used light or dark.
Our only color used is the warm grey Pantone 8003C hex #877A69

You will only need to design the homepage to win the competition, but the winning designer will be required to supply without extra charges:
1. Home page design
2. A second, standard page template design
3. An icon set in colors appropriate to the site that have icons to match the subjects in these pages:
https://trevanly.com.au/products/
https://trevanly.com.au/making-the-switch/
https://trevanly.com.au/why-trevanly/
We will create a single page version of the options on https://trevanly.com.au/solutions/
4.Any images used

Please avoid stock photos that are too common - e.g. smiling woman with headset, try to make the design stand out with simple images and well-designed layout.

Mid-size business clients

It Company

1 page

• Quil logo
• Use Quil color

```html
<!DOCTYPE html>
<html lang="en">
<head>
<meta charset="utf-8">
<title>Quil – IT outsourcing</title>
<link href="https://fonts.googleapis.com/css2?family=Roboto:wght@400;500&family=Open+Sans:wght@400;600&family=Lato:wght@400&display=swap" rel="stylesheet">
<style>
:root{
  --brand:#877a69;
  --brand-dark:#6f6456;
  --green:#8cc63f;
  --ink:#3a3a3a;
  --text:#6b6b6b;
  --light:#f2f2f2;
  --tile:#ebebeb;
  --review-bg:#f0f1f3;
  --logo-grey:#b9b9b9;
  --quote:#c4c6c9;
  --white:#ffffff;
}
*{margin:0;padding:0;box-sizing:border-box}
html,body{width:732px;height:1200px;overflow:hidden}
body{font-family:"Open Sans",sans-serif;color:var(--text);background:var(--white);position:relative}
a{color:inherit;text-decoration:none}

.hero{position:absolute;left:0;top:0;width:732px;height:350px;
  background:linear-gradient(100deg,#d9dde0 0%,#c9c3bb 35%,#e6e8ea 60%,#f1f2f3 100%)}
.hero-photo{position:absolute;inset:0}
.brand-name{position:absolute;left:82px;top:22px;display:flex;align-items:center;gap:6px;
  font-family:"Open Sans",sans-serif;font-weight:400;font-size:26px;line-height:1;color:var(--brand)}
.brand-dot{width:9px;height:9px;border-radius:50%;background:var(--brand)}
.tagline{position:absolute;right:199px;top:13px;font-family:"Lato",sans-serif;font-size:13.5px;color:var(--brand);letter-spacing:-.3px;white-space:nowrap}
.phone{position:absolute;left:549px;top:12px;font-family:"Roboto",sans-serif;font-size:14px;color:var(--ink);letter-spacing:.3px;white-space:nowrap}
.login{position:absolute;left:641px;top:14px}
.main-nav{position:absolute;top:38px;left:314px;display:flex;align-items:center;font-family:"Roboto",sans-serif;font-size:7.5px;color:var(--ink);letter-spacing:.2px}
.main-nav a{margin-right:13px}
.main-nav .cta{background:var(--green);color:var(--white);padding:4px 7px;border-radius:2px;margin-right:0}

.intro{position:absolute;left:0;top:350px;width:732px;height:220px;background:var(--light)}
.intro h2{position:absolute;left:78px;top:28px;font-family:"Roboto",sans-serif;font-weight:400;font-size:18px;color:var(--ink)}
.intro-copy{position:absolute;left:78px;top:59px;width:295px;font-size:8px;line-height:12.5px}
.intro-copy p+p{margin-top:12px}
.btn-more{position:absolute;left:78px;top:165px;width:67px;height:17px;background:var(--green);border-radius:3px;
  color:var(--white);font-family:"Roboto",sans-serif;font-weight:500;font-size:7px;display:flex;align-items:center;justify-content:center}
.intro-photo{position:absolute;left:392px;top:18px;width:261px;height:183px;background:linear-gradient(135deg,#dfe3e6,#a9a39b 60%,#6f6a63)}

.services{position:absolute;left:0;top:570px;width:732px;height:124px;display:flex}
.service{display:flex;flex-direction:column;align-items:center;justify-content:flex-end;padding-bottom:22px;
  font-family:"Roboto",sans-serif;font-size:13px;color:var(--brand);background:var(--tile)}
.service svg{margin-bottom:14px}
.service--data{width:255px}
.service--cloud{width:227px;background:var(--brand);color:var(--white)}
.service--support{width:250px}

.reviews{position:absolute;left:0;top:694px;width:732px;height:206px;background:var(--review-bg);text-align:center}
.reviews h2{margin-top:20px;font-family:"Roboto",sans-serif;font-weight:400;font-size:21px;color:var(--brand);letter-spacing:.2px}
.quote-mark{position:absolute;font-family:"Roboto",sans-serif;font-weight:500;font-size:64px;color:var(--quote);line-height:1}
.quote-open{left:106px;top:34px}
.quote-close{left:586px;top:64px}
.review-text{width:450px;margin:10px auto 0;font-size:8px;line-height:12.5px}
.avatar{width:58px;height:58px;border-radius:50%;margin:13px auto 0;background:radial-gradient(circle at 50% 40%,#c8c2ba,#8f8a84)}
.reviewer{margin-top:14px;font-family:"Roboto",sans-serif;font-size:9px;color:var(--ink)}
.reviewer-role{font-size:7px;margin-top:1px}

.partners{position:absolute;left:0;top:900px;width:732px;height:70px;background:var(--white)}
.partner{position:absolute;top:24px;font-family:"Roboto",sans-serif;font-weight:500;font-size:17px;color:var(--logo-grey)}

.site-footer{position:absolute;left:0;top:970px;width:732px;height:230px;background:linear-gradient(180deg,#8d7f6e,#867867)}
.footer-col{position:absolute;top:26px}
.footer-col h3{font-weight:600;font-size:15.5px;color:var(--white);margin-bottom:4px}
.footer-col a{display:block;font-size:10.5px;line-height:17.5px;color:#efe9e2}
.footer-rule{position:absolute;left:123px;top:160px;width:486px;height:1px;background:#b8ad9f}
.social{position:absolute;left:301px;top:174px;display:flex;gap:4.5px}
.social span{width:22px;height:22px;border-radius:50%;background:#e9e5e0}
.copyright{position:absolute;top:205px;width:100%;text-align:center;font-size:6.5px;color:#f1ece6}
</style>
</head>
<body>

<header class="hero">
  <div class="hero-photo" role="img" aria-label="Three young IT technicians discussing work at a desktop monitor in a bright office"></div>
  <a class="brand-name" href="#"><span class="brand-dot"></span>Quil</a>
  <div class="tagline">IT outsourcing the way it should be</div>
  <div class="phone">1300 482 915</div>
  <svg class="login" width="9" height="11" viewBox="0 0 9 11" aria-label="Login">
    <path d="M2 5V3.3a2.5 2.5 0 0 1 5 0V5" fill="none" stroke="#877a69" stroke-width="1.4"/>
    <rect x="0" y="5" width="9" height="6" rx="1" fill="#877a69"/>
  </svg>
  <nav class="main-nav">
    <a href="#">IT SUPPORT</a>
    <a href="#">VOIP</a>
    <a href="#">INTERNET AND DATA</a>
    <a href="#">CLOUD HOSTING</a>
    <a href="#">ABOUT</a>
    <a class="cta" href="#">CONTACT</a>
  </nav>
</header>

<section class="intro">
  <h2>The Right People</h2>
  <div class="intro-copy">
    <p>Not only does Quil have highly qualified people, with certifications from Norvane, Keltrix, National Telecom Standards Board amongst others, but importantly we can speak plain English and translate IT questions into a language you can understand and make decisions easier for you.</p>
    <p>We pride ourselves in our skill, integrity and ability to think and act in your best interests - that's what gets us customer referrals time after time.</p>
  </div>
  <a class="btn-more" href="#">READ MORE</a>
  <div class="intro-photo" role="img" aria-label="Colleagues reviewing a chart on a monitor together"></div>
</section>

<section class="services">
  <a class="service service--data" href="#">
    <svg width="56" height="58" viewBox="0 0 56 58">
      <path d="M0 0h44l12 12v46H0z" fill="#877a69"/>
      <rect x="12" y="0" width="28" height="20" fill="#ebebeb"/>
      <rect x="30" y="3" width="6" height="14" fill="#877a69"/>
      <rect x="10" y="28" width="30" height="3" fill="#ebebeb"/>
      <rect x="10" y="35" width="26" height="3" fill="#ebebeb"/>
      <rect x="10" y="42" width="30" height="3" fill="#ebebeb"/>
      <rect x="10" y="49" width="20" height="3" fill="#ebebeb"/>
    </svg>
    Data and Voice
  </a>
  <a class="service service--cloud" href="#">
    <svg width="68" height="56" viewBox="0 0 68 56">
      <path d="M16 52a14 14 0 0 1-2-28 18 18 0 0 1 34-6 13 13 0 0 1 6 34z" fill="#fff"/>
      <path d="M46 0l10 11h-6v8h-8v-8h-6z" fill="#fff"/>
      <path d="M24 28h8v10h6L28 50 18 38h6z" fill="#877a69"/>
      <path d="M25.5 29.5h5v10h4L28 47.5 21.5 39.5h4z" fill="#fff"/>
    </svg>
    Cloud Services
  </a>
  <a class="service service--support" href="#">
    <svg width="68" height="64" viewBox="0 0 68 64" fill="none" stroke="#877a69" stroke-width="2.5">
      <path d="M8 34V28a26 26 0 0 1 52 0v6"/>
      <rect x="2" y="30" width="10" height="20" rx="5"/>
      <rect x="56" y="30" width="10" height="20" rx="5"/>
      <path d="M61 50v4a6 6 0 0 1-6 6H38"/>
      <rect x="28" y="57" width="10" height="5" rx="2.5"/>
    </svg>
    Support
  </a>
</section>

<section class="reviews">
  <h2>CLIENTS REVIEWS</h2>
  <span class="quote-mark quote-open">&ldquo;</span>
  <span class="quote-mark quote-close">&rdquo;</span>
  <p class="review-text">Lorem ipsum dolor sit amet, consectetuer adipiscing elit, sed diam nonummy nibh euismod tincidunt ut laoreet dolore magna aliquam erat volutpat. Ut wisi enim ad minim veniam, quis nostrud eulla suscipit lobortis nisl ut aliquip ex ea commodo consequat.</p>
  <div class="avatar" role="img" aria-label="Portrait of the reviewer"></div>
  <div class="reviewer">Jhon Doe</div>
  <div class="reviewer-role">Senior Web Developer</div>
</section>

<section class="partners">
  <span class="partner" style="left:93px">THREADLY</span>
  <span class="partner" style="left:211px">SONARA</span>
  <span class="partner" style="left:322px">helmdesk</span>
  <span class="partner" style="left:440px">pixloop</span>
  <span class="partner" style="left:555px">testwise</span>
</section>

<footer class="site-footer" role="img" aria-label="Footer with a faint warm grey photo of a person working">
  <div class="footer-col" style="left:134px">
    <h3>Company</h3>
    <a href="#">About</a><a href="#">Careers</a><a href="#">Legal</a><a href="#">Privacy Policy</a>
  </div>
  <div class="footer-col" style="left:256px">
    <h3>Connect</h3>
    <a href="#">Friendnet</a><a href="#">Snapgrid</a><a href="#">Chirper</a><a href="#">Pinboardly</a>
  </div>
  <div class="footer-col" style="left:373px">
    <h3>Site Map</h3>
    <a href="#">Blog</a><a href="#">Companies</a><a href="#">FAQ</a><a href="#">Find A Candidate</a><a href="#">Find A Job</a>
  </div>
  <div class="footer-col" style="left:511px">
    <h3>Discover</h3>
    <a href="#">Newsroom</a><a href="#">Press</a><a href="#">Advertising</a><a href="#">Flight Schools</a><a href="#">Contact</a>
  </div>
  <div class="footer-rule"></div>
  <div class="social"><span></span><span></span><span></span><span></span><span></span></div>
  <p class="copyright">© Copyright 2017 Quil.net All Rights Reserved</p>
</footer>

</body>
</html>
```